Wordpress Design Project - Australian Solar Company wants to start FRESH!

About us

Bright Meadow are a renewable energy company based in Perth Australia, but we also have offices all over Asia. We specialise in offering renewable energy solutions (Solar PV Systems and LED Lighting) to residential and commercial customers.

Our current website: www.brightmeadowenergy.com.au

Our needs

This will be a replacement website as we are not happy with our current layout. We have an Australian company doing our SEO and they have recommended a new layout which we wish to go with.

We really want a professional and easy to navigate website that will assist in bringing in more enquiries and phone calls.

Content

We have all the content and will get the design winner to add this after we have chosen the design we like.
It is important that the call to actions are presented well and are visible these are things like the free quote form and our phone number.

The layout as we have advised has been based on SEO research so we wish it to be exactly the same unless otherwise stated.

Call to action

Our main objective of the new website is for people to come to the home page and see us as a professional and reliable company to deal with and enquire further.

We really want as many people as we can to convert to a lead. We want every person that comes to the website to enquire online or call us. We feel it is important to have a contact us/quote form on every page of the website.

Functional requirements

We have a chatterbook and vidstream account so links to these would be needed

Design assets

The logo needs to be displayed as shown in the website layout brief

Colours – we would like fresh, subdued colours that are professional and appealing to the eye. We ask that you do not take the colours from the logo.

Current website dislikes – the things we currently dislike about our current website is that it is hard to find information and there is no clear call to action. The colours are really unappealing as well as it looks cheap not professional.
The graphics that we require for the slider on the home page will have to be given after the winner is chosen but we want there to be three sliders on rotation

- Credibility builder (employee infront of solar panel) that encourages we use all our own employees not subcontractors
- Residential Slider – picture of a couple and solar panel system with a testimonial
- Commercial slider – picture of commercial system with “find out how you can install solar for free* at your business”

Design ideas

The website needs to be mobile friendly as well
It is going to be a total rebuild from the current website as our current website really isn’t working for us.

Target Market(s)

Target Audience

Our target audience are both residential and commercial clients
Residential – we want to attract home owners that are interested in reducing their electricity bill and helping the environment. Generally these people are between the ages of 28-50+ both male and female.

Commercial – We want to appeal to key decision makers within the commercial sphere. For example – CEOs, Company Directors, Operation managers and business owners of any industry. These people will be interested in reducing their electricity bills and creating a clean green image for their business.
Our target audience will generally come to our website to get information and enquire for a quote/ product information.

Industry/Entity Type

Residential

Requirements
Must have
• MUST BE LAID OUT LIKE THIS:

http://www.docuvault.com/doc/849302715/Website-Layout

Must have Enquire Now forms on every page that read:

Name
Phone Number
How did you hear about us
Message

```html
<!DOCTYPE html>
<html lang="en">
<head>
<meta charset="utf-8">
<title>Bright Meadow</title>
<link href="https://fonts.googleapis.com/css2?family=Source+Sans+3:wght@400;600;700&display=swap" rel="stylesheet">
<style>
:root{
  --green:#0a8f3c;
  --green-dark:#067a31;
  --orange:#f5a800;
  --orange-light:#fcc23a;
  --amber-text:#e89b00;
  --text:#6a6a6a;
  --heading:#555;
  --rule:#d8d8d8;
  --white:#fff;
}
*{box-sizing:border-box;margin:0;padding:0}
html,body{width:960px;height:1200px;overflow:hidden;background:var(--white)}
body{position:relative;font-family:"Source Sans 3",Arial,sans-serif;color:var(--text)}
.abs{position:absolute}
.top-strip{left:0;top:0;width:960px;height:4px;background:var(--green)}
.brand{left:96px;top:40px;display:flex;align-items:center;gap:10px}
.brand-mark{width:44px;height:44px;border-radius:50%;background:var(--orange)}
.brand-name{font-size:28px;font-weight:700;color:var(--green)}
.call-line{right:96px;top:32px;font-size:17px;font-weight:600;color:var(--green)}
.call-line span{color:var(--orange)}
.main-nav{left:304px;top:70px;width:560px;height:32px;background:linear-gradient(#fcc440,#f2a600);display:flex;justify-content:space-around;align-items:center}
.main-nav a{color:var(--white);font-size:11px;font-weight:600;text-decoration:none;letter-spacing:.2px}
.hero{left:0;top:116px;width:960px;height:336px;background:linear-gradient(160deg,#b9d6f0 0%,#3f7bc0 35%,#1d4f9a 60%,#a9c8e6 100%)}
.dots{left:465px;top:431px;display:flex;gap:4px}
.dots i{width:6px;height:6px;border-radius:50%;background:#9aa7b5;display:block}
.quote-box{left:648px;top:167px;width:208px;height:220px;background:var(--green);padding:12px 7px}
.quote-box h2{font-size:15px;font-weight:600;color:var(--white);margin:0 0 8px 4px}
.field{height:27px;background:var(--white);border:1px solid #cfd9d2;margin-bottom:10px;font-size:9px;color:#777;padding:8px 9px}
.btn{background:linear-gradient(var(--orange-light),var(--orange));color:var(--white);font-weight:600;display:inline-block}
.quote-box .btn{position:absolute;right:8px;bottom:10px;width:72px;height:25px;font-size:13px;text-align:center;line-height:25px}
.card{top:466px;width:184px}
.card h3{height:31px;background:linear-gradient(var(--green),var(--green-dark));color:var(--white);font-size:12.5px;font-weight:600;padding:7px 7px}
.card .pic{height:112px}
.card p{font-size:9.6px;line-height:14.4px;margin-top:6px;text-align:justify}
.card .btn{margin-top:10px;width:69px;height:24px;font-size:10px;line-height:24px;text-align:center}
.sec-title{font-size:14px;font-weight:600;color:var(--heading);text-transform:uppercase}
.rule{height:1px;background:var(--rule)}
.lead{left:95px;top:776px;width:505px;font-size:10.2px;line-height:14.4px;color:var(--amber-text)}
.body-copy{left:95px;top:820px;width:505px;font-size:9.6px;line-height:14.4px;text-align:justify}
.video{left:626px;top:779px;width:235px;height:150px;background:linear-gradient(90deg,#d9e2ea,#8a9aac 55%,#2d3a52)}
.play{left:710px;top:838px;width:64px;height:40px;border-radius:4px;background:rgba(255,255,255,.35)}
.foot-title{font-size:11px;font-weight:600;color:var(--heading);text-transform:uppercase}
.foot-list{list-style:none;font-size:10px;line-height:22.4px}
.member{display:flex;gap:10px;width:200px}
.member .pic{width:54px;height:54px;flex:none;background:linear-gradient(#e7e2dc,#9a8f86)}
.member h4{font-size:10.5px;font-weight:400;color:var(--green)}
.member p{font-size:8.8px;line-height:14.4px;text-align:justify}
.mini-field{width:192px;height:22px;border:1px solid #dcdcdc;font-size:9.6px;color:#777;padding:4px 8px;margin-bottom:4px}
.mini-submit{left:626px;top:1091px;width:56px;height:22px;font-size:11.5px;line-height:22px;text-align:center}
.contact{left:712px;top:984px;font-size:9.8px;line-height:16px;color:#555;font-weight:600}
.contact .org{color:var(--orange);margin-left:3px;margin-bottom:3px}
.copyright{left:94px;top:1147px;font-size:9.8px;color:#555}
.social{left:708px;top:1140px;display:flex;gap:7px}
.social i{display:block;width:25px;height:25px}
</style>
</head>
<body>
<div class="abs top-strip"></div>

<div class="abs brand"><span class="brand-mark"></span><span class="brand-name">Bright Meadow</span></div>
<div class="abs call-line">CAL US NOW! <span>1300 472 905</span></div>
<nav class="abs main-nav">
  <a>ABOUT</a><a>PRODUCTS</a><a>SERVICES</a><a>PROJECTS</a><a>MEDIA</a><a>INFORMATION</a><a>ENQUIRY</a><a>CONTACTS</a>
</nav>

<div class="abs hero" role="img" aria-label="Rows of solar panels under a blue sky with clouds"></div>
<div class="abs dots"><i></i><i></i><i></i></div>
<form class="abs quote-box">
  <h2>GET A QUOTE</h2>
  <div class="field">Name</div>
  <div class="field">Phone Number</div>
  <div class="field">How did you hear about us</div>
  <div class="field">Message</div>
  <span class="btn">SUBMIT</span>
</form>

<div class="abs card" style="left:96px">
  <h3>RESIDENTIAL SOLAR POWER</h3>
  <div class="pic" role="img" aria-label="Solar panels on a house roof" style="background:linear-gradient(#9fc1df,#3a4c72 60%,#7a4b35)"></div>
  <p>Sed ut perspiciatis unde omnis iste natus error ptatem accustiu doloremque laudantium, totam rem aperiam, eaque ipsa quae ab illo inventore varchitecto</p>
  <span class="btn">READ MORE</span>
</div>
<div class="abs card" style="left:290px">
  <h3>COMMERCIAL SOLAR POWER</h3>
  <div class="pic" role="img" aria-label="Large commercial solar panel array" style="background:linear-gradient(#8a9676,#2d3c5e 55%,#8d9196)"></div>
  <p>Sed ut perspiciatis unde omnis iste natus error ptatem accustiu doloremque laudantium, totam rem aperiam, eaque ipsa quae ab illo inventore varchitecto</p>
  <span class="btn">READ MORE</span>
</div>
<div class="abs card" style="left:485px">
  <h3>AIR CONDITIONING W/A</h3>
  <div class="pic" role="img" aria-label="Wall air conditioner with a remote control" style="background:linear-gradient(#f1f3f4,#d3d8dc)"></div>
  <p>Sed ut perspiciatis unde omnis iste natus error ptatem accustiu doloremque laudantium, totam rem aperiam, eaque ipsa quae ab illo inventore varchitecto</p>
  <span class="btn">READ MORE</span>
</div>
<div class="abs card" style="left:679px">
  <h3>PERTH LED LIGHTING</h3>
  <div class="pic" role="img" aria-label="LED light bulb close up" style="background:radial-gradient(circle at 60% 40%,#f4f2e4,#c9d3e3 55%,#2b4aa8)"></div>
  <p>Sed ut perspiciatis unde omnis iste natus error ptatem accustiu doloremque laudantium, totam rem aperiam, eaque ipsa quae ab illo inventore varchitecto</p>
  <span class="btn">READ MORE</span>
</div>

<h2 class="abs sec-title" style="left:96px;top:736px">Welcome to Bright Meadow!</h2>
<div class="abs rule" style="left:96px;top:766px;width:504px"></div>
<p class="abs lead">Sed ut perspiciatis unde omnis iste natus error ptatem accustiu doloremque laudantium, totam rem aperiam, eaque ipsa quae ab illo inventore varchitecto</p>
<p class="abs body-copy">Sed ut perspiciatis unde omnis iste natus error ptatem accustiu doloremque laudantium, totam rem aperiam, eaque ipsa quae ab illo inventore varchitecto Sed ut perspiciatis unde omnis iste natus error ptatem accustiu doloremque laudantium, totam rem aperiam, eaque ipsa quae ab illo inventore varchitecto Sed ut perspiciatis unde omnis iste natus error ptatem accustiu doloremque laudantium, totam rem aperiam, eaque ipsa quae ab illo inventore varchitecto Sed ut perspiciatis unde omnis iste natus error ptatem accustiu doloremque laudantium, totam rem aperiam, eaque ipsa quae ab illo inventore varchitecto Sed ut perspiciatis unde omnis iste natus error ptatem accustiu doloremque laudantium, totam rem aperiam, eaque ipsa quae ab illo inventore varchitecto Sed ut perspiciatis unde omnis</p>

<h2 class="abs sec-title" style="left:623px;top:736px">Testimonials</h2>
<div class="abs rule" style="left:623px;top:766px;width:241px"></div>
<div class="abs video" role="img" aria-label="Testimonial video still of a business professional in an office"></div>
<div class="abs play"><svg width="64" height="40" viewBox="0 0 64 40"><polygon points="26,11 26,29 41,20" fill="#fff" opacity=".85"/></svg></div>

<div class="abs rule" style="left:96px;top:952px;width:768px"></div>

<h3 class="abs foot-title" style="left:96px;top:963px">Product &amp; Services</h3>
<ul class="abs foot-list" style="left:96px;top:984px">
  <li>Solar PV Systems</li><li>LED Lighting</li><li>Air Conditioning</li><li>Solar Leasing</li><li>Electrical Services</li><li>Refrigeration Systems</li>
</ul>

<h3 class="abs foot-title" style="left:271px;top:963px">Memberships</h3>
<div class="abs member" style="left:272px;top:984px">
  <div class="pic" role="img" aria-label="Member portrait photo"></div>
  <div><h4>Sed ut perspiciatis unde</h4><p>Sed ut perspiciatis unde omnis iste natus error ptatem accustiu doloremque laudantium,</p></div>
</div>
<div class="abs member" style="left:272px;top:1057px">
  <div class="pic" role="img" aria-label="Member portrait photo"></div>
  <div><h4>Sed ut perspiciatis unde</h4><p>Sed ut perspiciatis unde omnis iste natus error ptatem accustiu doloremque laudantium,</p></div>
</div>

<h3 class="abs foot-title" style="left:490px;top:963px">Request Quotation</h3>
<form class="abs" style="left:490px;top:984px">
  <div class="mini-field">Name</div>
  <div class="mini-field">Phone Number</div>
  <div class="mini-field">How did you hear about us</div>
  <div class="mini-field">Message</div>
</form>
<span class="abs btn mini-submit">SUBMIT</span>

<h3 class="abs foot-title" style="left:711px;top:963px">Contact Info</h3>
<div class="abs contact">
  <div class="org">BRIGHT MEADOW</div>
  U4 18 Kestrel Road<br>Willow Park, WA 6190<br><br>
  Phone: (08) 6391 7724<br>Fax: (08) 6391 7725<br>Email: sales@brightmeadowenergy.com.au
</div>

<div class="abs rule" style="left:96px;top:1129px;width:768px"></div>
<p class="abs copyright">Copyright © 2013 Bright Meadow. All rights reserved.</p>
<div class="abs social" aria-label="Social links">
  <i style="background:#2d4f9e" title="chatterbook"></i>
  <i style="background:#1fa5e0"></i>
  <i style="background:#d0121c"></i>
  <i style="background:#b21611" title="vidstream"></i>
  <i style="background:#d9483b"></i>
</div>
</body>
</html>
```